Verdant Banner Design

We need 3 Banners for our superfood supplement e-commerce store.

1. Banner that advertises the food combining chart Dimensions 417 × 464 https://verdantlift.net/content/11-food-combining-rules

2. We need a banner that advertises our subscription program. (Dimensions 388 × 219)

3. We need a banner that highlights our ingredients. (Dimensions 388 × 215)

Our website: https://verdantlift.net/

1. The sizes are in dimensions.

2. Yes the banners are for our website, replacing the ones on the front page now https://verdantlift.net/

Content of Banners

1. Advertisng the food combining chart.

2. Advertising our Subscription program.

3 Advertising our ingredients.

Just use words like:

"Combine the right foods"

Target Market(s)

Organic Superfood Supplement

Contact Information for Business Card

The Business card has to be double sided and must have our logo

Colors

Designer to choose colors to be used in the design.

Requirements
Must have
• 1. You can use the attached images or not, it is up to you, please be creative.
• 2. Please provide the Raw AI files, and also give it in the following formats: JPEG, PNG,
• 3. I have added a file in the brief called subscription image please use to get an idea of the type of banner we are looking for, of course using our product images
Nice to have
• 1. Please show business card design as well, this will help us decide to choose you.
• 2. Please read the ingredients on the product itself, and if you can use some images for the ingredient banner that would be good.
• 3. The business card should have the following:
• Name: Rupert Halvey
• Title: Co-Founder
• Address: Baldwin, NY
• Logo (see attached)
• Phone #: 855-640-3918
• Mobile #: 646-508-2274
• Email: info@verdantlift.net
• Website: www.verdantlift.net
Should not have
• No meat or dairy products in your images

```html
<!DOCTYPE html>
<html lang="en">
<head>
<meta charset="utf-8">
<title>Verdant Foods For Todays Lifestyle</title>
<link href="https://fonts.googleapis.com/css2?family=Libre+Baskerville:wght@700&display=swap" rel="stylesheet">
<style>
  :root {
    --gold-light: #caa634;
    --gold-dark: #8c6e12;
    --green-light: #b9d736;
    --green-mid: #8dbb2a;
    --green-dark: #5e8f16;
    --headline-green: #2f4b0f;
    --white: #ffffff;
    --frame-light: #e4e4e4;
    --frame-dark: #8d8d8d;
    --panel-left: #e25c5a;
    --panel-right: #da4c4b;
    --panel-bottom: #c92a2b;
  }
  html, body {
    margin: 0;
    padding: 0;
    overflow: hidden;
    background: #ffffff;
  }
  .banner {
    position: relative;
    width: 1078px;
    height: 1200px;
    overflow: hidden;
    font-family: "Libre Baskerville", Georgia, serif;
  }
  .banner-art {
    position: absolute;
    inset: 0;
    width: 1078px;
    height: 1200px;
  }
  .headline {
    position: absolute;
    top: 22px;
    left: 0;
    width: 100%;
    margin: 0;
    text-align: center;
    color: var(--white);
    font-size: 86px;
    line-height: 1.04;
    font-weight: 700;
    text-shadow: 3px 4px 5px rgba(60, 40, 0, 0.75);
    letter-spacing: 0.5px;
  }
  .brand {
    position: absolute;
    left: 800px;
    top: 858px;
    display: flex;
    align-items: center;
    gap: 12px;
  }
  .brand-dot {
    width: 30px;
    height: 30px;
    border-radius: 50%;
    background: var(--headline-green);
  }
  .brand-name {
    font-size: 50px;
    font-weight: 700;
    color: var(--headline-green);
  }
  .tagline {
    position: absolute;
    bottom: 28px;
    left: 0;
    width: 100%;
    margin: 0;
    text-align: center;
    color: var(--headline-green);
    font-size: 66px;
    font-weight: 700;
    text-shadow: 2px 3px 3px rgba(255, 255, 255, 0.55);
  }
</style>
</head>
<body>
<main class="banner">
  <svg class="banner-art" viewBox="0 0 1078 1200" xmlns="http://www.w3.org/2000/svg">
    <defs>
      <linearGradient id="gold-band" x1="0" y1="0" x2="0" y2="1">
        <stop offset="0" stop-color="var(--gold-light)"/>
        <stop offset="1" stop-color="var(--gold-dark)"/>
      </linearGradient>
      <linearGradient id="green-field" x1="0" y1="0" x2="1" y2="1">
        <stop offset="0" stop-color="var(--green-light)"/>
        <stop offset="0.6" stop-color="var(--green-mid)"/>
        <stop offset="1" stop-color="var(--green-dark)"/>
      </linearGradient>
      <linearGradient id="heart-frame" x1="0" y1="0" x2="1" y2="1">
        <stop offset="0" stop-color="var(--frame-light)"/>
        <stop offset="0.5" stop-color="var(--frame-dark)"/>
        <stop offset="1" stop-color="#5a5a5a"/>
      </linearGradient>
      <radialGradient id="citrus-tones" cx="0.5" cy="0.5" r="0.6">
        <stop offset="0" stop-color="#f7c21e"/>
        <stop offset="0.6" stop-color="#f08a1c"/>
        <stop offset="1" stop-color="#8fbf3a"/>
      </radialGradient>
      <radialGradient id="orchard-tones" cx="0.5" cy="0.5" r="0.6">
        <stop offset="0" stop-color="#e0493a"/>
        <stop offset="0.6" stop-color="#f0a35a"/>
        <stop offset="1" stop-color="#3a2140"/>
      </radialGradient>
      <radialGradient id="melon-tones" cx="0.5" cy="0.5" r="0.6">
        <stop offset="0" stop-color="#3f7a2a"/>
        <stop offset="0.6" stop-color="#f2a45a"/>
        <stop offset="1" stop-color="#c6d98a"/>
      </radialGradient>
      <clipPath id="heart-inner">
        <path d="M540 425 C495 350 410 335 310 343 C215 352 165 420 170 495 C176 600 285 705 540 1015 C795 705 904 600 910 495 C915 420 865 352 770 343 C670 335 585 350 540 425 Z"/>
      </clipPath>
    </defs>

    <rect class="green-field" x="0" y="0" width="1078" height="1200" fill="url(#green-field)"/>
    <path class="gold-band" d="M0 0 H1078 V360 Q560 250 0 330 Z" fill="url(#gold-band)"/>
    <path class="white-swoosh-top" d="M0 330 Q560 250 1078 360 V450 Q560 330 0 430 Z" fill="var(--white)"/>
    <path class="olive-swoosh-bottom" d="M0 1040 Q560 950 1078 900 V960 Q560 1010 0 1090 Z" fill="var(--gold-dark)" opacity="0.75"/>
    <path class="white-swoosh-bottom" d="M0 1010 Q560 950 1078 880 V930 Q560 990 0 1060 Z" fill="var(--white)"/>

    <g class="heart">
      <path class="heart-frame" d="M540 395 C490 315 400 298 300 308 C190 318 128 400 133 490 C140 612 262 725 540 1068 C818 725 940 612 947 490 C952 400 890 318 780 308 C680 298 590 315 540 395 Z" fill="url(#heart-frame)"/>
      <g clip-path="url(#heart-inner)">
        <polygon class="panel-left" points="0,0 540,0 540,640 0,740" fill="var(--panel-left)"/>
        <polygon class="panel-right" points="540,0 1078,0 1078,740 540,640" fill="var(--panel-right)"/>
        <polygon class="panel-bottom" points="0,740 540,640 1078,740 1078,1200 0,1200" fill="var(--panel-bottom)"/>
        <path class="panel-dividers" d="M540 300 V640 M0 740 L540 640 L1078 740" stroke="#9e2020" stroke-width="4" fill="none"/>
        <ellipse class="citrus-photo" role="img" aria-label="Assorted citrus fruits: limes, oranges, lemons and grapefruit" cx="345" cy="505" rx="170" ry="125" fill="url(#citrus-tones)"/>
        <ellipse class="orchard-photo" role="img" aria-label="Strawberries, apple, pear, peaches and blackberries" cx="745" cy="495" rx="170" ry="135" fill="url(#orchard-tones)"/>
        <ellipse class="melon-photo" role="img" aria-label="Watermelon and sliced cantaloupe melons" cx="545" cy="765" rx="145" ry="115" fill="url(#melon-tones)"/>
      </g>
    </g>
  </svg>

  <h1 class="headline">Verdant Foods For<br>Todays Lifestyle</h1>

  <div class="brand">
    <span class="brand-dot"></span>
    <span class="brand-name">Verdant</span>
  </div>

  <p class="tagline">Combine The Right Foods</p>
</main>
</body>
</html>
```